Holiday PROMO Flyer for Healthy Restaurant

Hi ! We need a holiday style promo flyer for Verandel . Please have a holiday vibe type of design in the background. Include at least 1 of the photos that I provide, and our logo of course. This promo is for a new package that we will be offering until December 31st 2022.

It will have a promo of some type of design that says the following in a creative way:
" HOLIDAY PACKAGE PROMO!"
Buy our holiday package of $500 and receive a $100 gift card!" (THIS SHOULD BE VERY NOTICEABLE AS THIS IS THE ACTUAL PROMO)
Our biggest promo to date.
Offer ends December 31st, 2022.

Take a look at our website to stay consistant with the brand as well.

Industry/Entity Type

Restaurant

Requirements
Must have
• Logo, food photo and gift card photo

```html
<!DOCTYPE html>
<html lang="en">
<head>
<meta charset="utf-8">
<title>Verandel Holiday Package Promo Flyer</title>
<link href="https://fonts.googleapis.com/css2?family=Oswald:wght@500;700&family=Cabin:wght@500&display=swap" rel="stylesheet">
<style>
  :root {
    --page: #ffffff;
    --slate: #37485a;
    --slate-deep: #2e3d4d;
    --forest: #27452f;
    --forest-dark: #1f3a27;
    --lime: #b8cc2c;
    --leaf: #8dc63f;
    --ink: #1d2419;
    --white: #ffffff;
    --navy: #1f2f5a;
    --wood-light: #e7e9ea;
    --wood-mid: #b9c0c4;
    --plate-light: #f1eee8;
    --plate-warm: #dcc9ad;
    --logo-grey: #8a8c8e;
  }
  * { box-sizing: border-box; margin: 0; padding: 0; }
  html, body { width: 1200px; height: 1000px; overflow: hidden; background: var(--page); }
  .flyer {
    position: absolute; left: 262px; top: 60px; width: 676px; height: 878px;
    overflow: hidden;
    background: linear-gradient(180deg, var(--slate) 0%, var(--slate-deep) 62%);
    box-shadow: 0 4px 14px rgba(0,0,0,0.18);
    font-family: "Oswald", sans-serif;
  }
  .backdrop-drape {
    position: absolute; inset: 0 0 auto 0; height: 460px;
    background:
      radial-gradient(ellipse 180px 420px at 0% 30%, var(--forest) 60%, transparent 61%),
      radial-gradient(ellipse 160px 420px at 100% 30%, var(--forest) 60%, transparent 61%),
      radial-gradient(ellipse 420px 160px at 50% 0%, var(--forest-dark) 60%, transparent 61%);
    opacity: 0.85;
  }
  .wood-surface {
    position: absolute; left: 0; right: 0; top: 530px; bottom: 0;
    background: linear-gradient(180deg, rgba(185,192,196,0) 0%, var(--wood-mid) 30%, var(--wood-light) 75%);
  }
  .headline {
    position: absolute; left: 0; right: 0; text-align: center; text-transform: uppercase;
    line-height: 1; font-weight: 700; letter-spacing: 1px;
  }
  .headline-main { top: 49px; font-size: 94px; color: var(--lime); }
  .headline-sub { top: 138px; font-size: 52px; color: var(--white); }
  .offer-band {
    position: absolute; left: 83px; top: 212px; width: 505px; height: 71px;
    background: var(--leaf); color: var(--ink);
    display: flex; align-items: center; justify-content: center;
    font-size: 37px; font-weight: 700; text-transform: uppercase;
  }
  .offer-figure { position: absolute; top: 298px; text-align: center; }
  .offer-figure .amount { display: block; font-size: 94px; line-height: 1; font-weight: 700; color: var(--white); }
  .offer-figure .caption { display: block; margin-top: 2px; font-size: 27px; line-height: 1; font-weight: 700; color: var(--lime); text-transform: uppercase; }
  .offer-figure.spend { left: 112px; width: 212px; }
  .offer-figure.reward { left: 364px; width: 200px; }
  .offer-divider { position: absolute; left: 349px; top: 318px; width: 2px; height: 102px; background: rgba(255,255,255,0.7); }
  .promo-note {
    position: absolute; left: 0; right: 0; top: 440px; text-align: center;
    font-family: "Cabin", sans-serif; font-weight: 500; font-size: 33px; line-height: 37px; color: var(--white);
  }
  .gift-card {
    position: absolute; left: 58px; top: 544px; width: 258px; height: 168px;
    border-radius: 14px; background: var(--navy); overflow: hidden; z-index: 2;
  }
  .gift-card .band-v { position: absolute; left: 40px; top: 0; bottom: 0; width: 10px; background: var(--leaf); }
  .gift-card .band-h { position: absolute; left: 0; right: 0; top: 28px; height: 10px; background: var(--leaf); }
  .gift-card .card-label {
    position: absolute; left: 16px; top: 130px; transform: rotate(-90deg); transform-origin: left top;
    font-family: "Cabin", sans-serif; font-size: 12px; letter-spacing: 2px; color: var(--leaf);
  }
  .gift-card .card-name {
    position: absolute; left: 62px; top: 72px;
    font-family: "Oswald", sans-serif; font-weight: 700; font-size: 36px; line-height: 1; color: var(--white); letter-spacing: 1px;
  }
  .food-photo {
    position: absolute; left: 228px; top: 562px; width: 448px; height: 316px;
    border-radius: 224px 0 0 160px;
    background: linear-gradient(135deg, var(--plate-light) 0%, var(--plate-warm) 100%);
  }
  .brand-plate {
    position: absolute; left: 58px; top: 742px; width: 258px; height: 74px;
    background: var(--white); border: 2px solid var(--slate);
    display: flex; align-items: center; justify-content: center; z-index: 2;
  }
  .brand-plate .brand-name {
    font-family: "Oswald", sans-serif; font-weight: 700; font-size: 44px; line-height: 1; color: var(--logo-grey); letter-spacing: 1px;
  }
</style>
</head>
<body>
  <main class="flyer">
    <div class="backdrop-drape" role="img" aria-label="Dark green holiday drapery backdrop"></div>
    <div class="wood-surface" role="img" aria-label="Whitewashed wooden tabletop"></div>

    <h1 class="headline headline-main">Holiday</h1>
    <h2 class="headline headline-sub">Package Promo!</h2>

    <div class="offer-band">Buy our holiday package of</div>

    <div class="offer-figure spend">
      <span class="amount">+500</span>
      <span class="caption">and receive a</span>
    </div>
    <div class="offer-divider"></div>
    <div class="offer-figure reward">
      <span class="amount">+100</span>
      <span class="caption">gift card!</span>
    </div>

    <p class="promo-note">Our biggest promo to date.<br>Offer ends December 31st, 2022.</p>

    <div class="food-photo" role="img" aria-label="Photo of a plated meal: blackened chicken with cream sauce, mashed potatoes and bok choy"></div>

    <div class="gift-card">
      <div class="band-v"></div>
      <div class="band-h"></div>
      <span class="card-label">GIFT CARD</span>
      <span class="card-name">Verandel</span>
    </div>

    <div class="brand-plate">
      <span class="brand-name">Verandel</span>
    </div>
  </main>
</body>
</html>
```